3 Business Card designs for a company with multiple services

We are a company that has 3 main services:

1) Security - CCTV & Alarm Sepcialists
2) Broadcast - Broadcast Sales and Technical Services
3) Distribution - Quality Products, Quality Service

The broadcast service is for Video Broadcast.

I will include our logos for each service.

I would like to also create a business card design for 7QK in general (see main logo).

Each card will be two-sided. On the front I would think it would include Logo, Name, Posistion and Mobile (and possibly email). And possibly our main number (which may be something like 1800 639 415)

On the back it MUST include a "lined" section to be able to write short quotes / prices.

Then include more details like Phone: 1800 639 415 Fax: 1800 639 412 Postal: PO Box 731, Tallowen, QLD Australia 4290 Website: www.7qk.com.au

We would like a fresh, inovative card design with that "wow check this out" feel about it.

Look forward to seeing what you can do! :)

Corey

Industry/Entity Type

Business

Requirements
Must have
• Quote section on the back!
Editable files.

```html
<!DOCTYPE html>
<html lang="en">
<head>
<meta charset="utf-8">
<title>7QK Business Cards</title>
<link href="https://fonts.googleapis.com/css2?family=Arimo:wght@400;700&display=swap" rel="stylesheet">
<style>
  :root {
    --page: #000000;
    --card-dark: #2b2b2b;
    --card-darker: #1c1c1c;
    --white: #ffffff;
    --ink: #1a1a1a;
    --red-light: #ee4a22;
    --red-dark: #a8151b;
    --blue-light: #2aa3e6;
    --blue-dark: #1b2f9a;
    --steel-light: #c9c9c9;
    --steel-dark: #7d7d7d;
    --gold-light: #f6c431;
    --gold-dark: #d98a0b;
    --muted: #d8d8d8;
  }
  * { margin: 0; padding: 0; box-sizing: border-box; }
  html, body { width: 1200px; height: 900px; overflow: hidden; background: var(--page); }
  body { position: relative; font-family: "Arimo", Arial, sans-serif; color: var(--white); }

  .card {
    position: absolute; width: 500px; height: 286px; overflow: hidden;
    background: linear-gradient(160deg, #333 0%, var(--card-dark) 45%, var(--card-darker) 100%);
  }
  .card--front { left: 74px; border-radius: 22px 0 0 0; }
  .card--back { left: 620px; border-radius: 0 22px 0 0; }
  .row-security { top: 140px; }
  .row-distribution { top: 470px; }

  .brand {
    position: absolute; left: 18px; top: 20px; height: 62px; width: 194px;
    background: var(--white); border-radius: 4px;
    display: flex; align-items: center; gap: 10px; padding: 0 10px;
    z-index: 2;
  }
  .brand-square { width: 36px; height: 36px; border-radius: 3px; flex: none; }
  .theme-security .brand-square { background: var(--red-dark); }
  .theme-distribution .brand-square { background: var(--blue-dark); }
  .brand-name { font-size: 20px; font-weight: 700; color: var(--ink); line-height: 1.05; }

  .band { position: absolute; left: 0; right: 0; z-index: 1; }
  .theme-security .band { background: linear-gradient(90deg, var(--red-light), var(--red-dark)); }
  .theme-distribution .band { background: linear-gradient(90deg, var(--blue-light), var(--blue-dark)); }
  .card--front .band { top: 106px; height: 126px; }
  .card--back .band { top: 120px; bottom: 0; }
  .theme-distribution.card--back .band { background: linear-gradient(90deg, var(--blue-dark), var(--blue-light)); }

  .person { position: absolute; left: 28px; top: 118px; z-index: 2; }
  .person-name { font-size: 24px; font-weight: 700; }
  .person-role { font-size: 14px; margin-top: 6px; }
  .contact-list { list-style: none; margin-top: 18px; font-size: 12px; line-height: 15px; }
  .contact-list li { display: flex; align-items: center; gap: 6px; }
  .contact-list svg { width: 11px; height: 11px; fill: var(--white); }

  .footer-strip {
    position: absolute; left: 0; right: 0; bottom: 0; height: 30px;
    background: var(--card-darker); z-index: 1;
  }
  .website {
    position: absolute; right: 26px; bottom: 8px; z-index: 3;
    font-size: 13px; letter-spacing: 2.5px; color: var(--muted);
  }

  .emblem-lock {
    position: absolute; border-radius: 14px; z-index: 2;
    background: linear-gradient(180deg, var(--steel-light), var(--steel-dark));
  }
  .emblem-globe {
    position: absolute; border-radius: 50%; z-index: 2;
    background: radial-gradient(circle at 40% 35%, var(--gold-light), var(--gold-dark));
  }
  .card--front .emblem-lock { left: 344px; top: 90px; width: 120px; height: 162px; }
  .card--front .emblem-globe { left: 322px; top: 94px; width: 160px; height: 160px; }
  .card--back .emblem-lock { left: 14px; top: 196px; width: 54px; height: 82px; border-radius: 8px; }
  .card--back .emblem-globe { left: 14px; top: 194px; width: 80px; height: 80px; }

  .back-details {
    position: absolute; left: 300px; top: 20px;
    font-size: 11px; line-height: 13px; color: var(--white);
  }
  .note-box {
    position: absolute; left: 100px; top: 126px; width: 386px; height: 124px; z-index: 2;
    background: var(--white); border-radius: 12px; border: 2px solid rgba(0,0,0,0.25);
    padding: 12px 16px; color: var(--ink); font-size: 15px; font-weight: 700;
  }
  .card--back .website { bottom: 6px; right: 160px; color: var(--white); }
</style>
</head>
<body>

  <section class="card card--front row-security theme-security">
    <div class="brand"><span class="brand-square"></span><span class="brand-name">7QK<br>Security</span></div>
    <div class="band"></div>
    <div class="person">
      <h2 class="person-name">Sam Rivers</h2>
      <p class="person-role">Field Manager</p>
      <ul class="contact-list">
        <li><svg viewBox="0 0 12 12"><rect x="3" y="0" width="6" height="12" rx="1"/></svg>0412 555 019</li>
        <li><svg viewBox="0 0 12 12"><path d="M1 4 Q6 0 11 4 L9 6 L8 4 L4 4 L3 6 Z M2 7 H10 V11 H2 Z"/></svg>1800 639 415</li>
        <li><svg viewBox="0 0 12 12"><path d="M0 2 H12 V10 H0 Z"/></svg>sam@7qk.com.au</li>
      </ul>
    </div>
    <div class="footer-strip"></div>
    <div class="emblem-lock" role="img" aria-label="Large padlock illustration"></div>
    <p class="website">www.7qk.com.au</p>
  </section>

  <section class="card card--back row-security theme-security">
    <div class="brand"><span class="brand-square"></span><span class="brand-name">7QK<br>Security</span></div>
    <p class="back-details">Phone: 1800 639 415<br>Fax: 1800 639 412<br>Postal: PO Box 731, Tallowen<br>QLD Australia 4290</p>
    <div class="band"></div>
    <div class="note-box">Note :</div>
    <div class="emblem-lock" role="img" aria-label="Small padlock illustration"></div>
    <p class="website">www.7qk.com.au</p>
  </section>

  <section class="card card--front row-distribution theme-distribution">
    <div class="brand"><span class="brand-square"></span><span class="brand-name">7QK<br>Distribution</span></div>
    <div class="band"></div>
    <div class="person">
      <h2 class="person-name">Sam Rivers</h2>
      <p class="person-role">Field Manager</p>
      <ul class="contact-list">
        <li><svg viewBox="0 0 12 12"><rect x="3" y="0" width="6" height="12" rx="1"/></svg>0412 555 019</li>
        <li><svg viewBox="0 0 12 12"><path d="M1 4 Q6 0 11 4 L9 6 L8 4 L4 4 L3 6 Z M2 7 H10 V11 H2 Z"/></svg>1800 639 415</li>
        <li><svg viewBox="0 0 12 12"><path d="M0 2 H12 V10 H0 Z"/></svg>sam@7qk.com.au</li>
      </ul>
    </div>
    <div class="footer-strip"></div>
    <div class="emblem-globe" role="img" aria-label="Large golden globe illustration"></div>
    <p class="website">www.7qk.com.au</p>
  </section>

  <section class="card card--back row-distribution theme-distribution">
    <div class="brand"><span class="brand-square"></span><span class="brand-name">7QK<br>Distribution</span></div>
    <p class="back-details">Phone: 1800 639 415<br>Fax: 1800 639 412<br>Postal: PO Box 731, Tallowen<br>QLD Australia 4290</p>
    <div class="band"></div>
    <div class="note-box">Note :</div>
    <div class="emblem-globe" role="img" aria-label="Small golden globe illustration"></div>
    <p class="website">www.7qk.com.au</p>
  </section>

</body>
</html>
```